Need a Facebook image for childcare advertisement

We are after a design for Facebook advertisement for childcare and kindergarten centre enrolments for 2023.

I have attached a previous flyer that we have in pdf format. The new logo is also attached with this brief.

All other information is still current as per the attached flyer.

You can use same colours as per attached flyer. I will also attached some stock images that you can select to use for the design.

our website for your reference:

https://tallowmere-vale.com.au

```html
<!DOCTYPE html>
<html lang="en">
<head>
<meta charset="utf-8">
<title>Tallowmere Vale – Kindergarten 2023 Enrolments</title>
<link rel="stylesheet" href="https://fonts.googleapis.com/css2?family=Jost:wght@700;800&display=swap">
<style>
  :root {
    --navy: #07073f;
    --red: #ee3b3b;
    --white: #ffffff;
    --orange: #f5822a;
    --green: #6cbf3c;
    --blue: #1f4e9a;
    --purple: #8e3399;
    --ribbon-purple: #b466c4;
    --ribbon-cyan: #7fd0dc;
    --ribbon-pink: #e9b6dc;
    --photo-warm: #e9b98e;
    --photo-cool: #c9c4a8;
  }
  html, body {
    margin: 0;
    padding: 0;
    width: 1200px;
    height: 628px;
    overflow: hidden;
    background: var(--navy);
  }
  .ad {
    position: relative;
    width: 1200px;
    height: 628px;
    overflow: hidden;
    font-family: "Jost", "Futura", sans-serif;
  }
  .ad__art {
    position: absolute;
    inset: 0;
    width: 1200px;
    height: 628px;
    display: block;
  }
  .brand__name {
    fill: var(--white);
    font-weight: 800;
    font-size: 50px;
    letter-spacing: 1px;
  }
  .brand__tagline {
    fill: var(--white);
    font-weight: 700;
    font-size: 24px;
  }
  .headline {
    font-weight: 800;
    font-size: 64px;
    stroke: var(--white);
    stroke-width: 5px;
    paint-order: stroke fill;
    stroke-linejoin: round;
  }
  .headline__word { fill: var(--red); }
  .headline__digit--orange { fill: var(--orange); }
  .headline__digit--green { fill: var(--green); }
  .headline__digit--blue { fill: var(--blue); }
  .headline__digit--purple { fill: var(--purple); }
  .subline {
    fill: var(--white);
    font-weight: 700;
    font-size: 62px;
  }
</style>
</head>
<body>
<main class="ad">
  <svg class="ad__art" viewBox="0 0 1200 628" xmlns="http://www.w3.org/2000/svg">
    <defs>
      <linearGradient id="photoTone" x1="0" y1="0" x2="1" y2="0.4">
        <stop offset="0" stop-color="#d98a3c"/>
        <stop offset="0.3" stop-color="var(--photo-warm)"/>
        <stop offset="0.6" stop-color="var(--photo-cool)"/>
        <stop offset="1" stop-color="#8a5a50"/>
      </linearGradient>
    </defs>

    <rect class="hero-photo" x="0" y="0" width="1200" height="420" fill="url(#photoTone)"
          role="img" aria-label="Photo of young children in a bright classroom, a girl holding a red pointer"/>

    <g class="ribbons">
      <path d="M0,418 Q600,400 1200,-10 L1200,40 Q600,430 0,420 Z" fill="var(--ribbon-purple)" opacity="0.8"/>
      <path d="M0,410 Q620,420 1200,50 L1200,38 Q620,415 0,410 Z" fill="var(--ribbon-cyan)"/>
      <path d="M0,405 Q640,410 1200,0 L1200,14 Q640,420 0,408 Z" fill="var(--ribbon-pink)" opacity="0.9"/>
    </g>

    <path class="panel" d="M0,412 Q600,444 1200,40 L1200,628 L0,628 Z" fill="var(--navy)"/>

    <g class="brand">
      <text class="brand__name" x="912" y="290" text-anchor="middle">TALLOWMERE VALE</text>
      <text class="brand__tagline" x="911" y="370" text-anchor="middle" textLength="440" lengthAdjust="spacingAndGlyphs">EARLY CHILDHOOD LEARNING CENTRE</text>
    </g>

    <text class="headline" x="78" y="484" textLength="1050" lengthAdjust="spacingAndGlyphs"><tspan class="headline__word">Kindergarten </tspan><tspan class="headline__digit--orange">2</tspan><tspan class="headline__digit--green">0</tspan><tspan class="headline__digit--blue">2</tspan><tspan class="headline__digit--purple">3</tspan><tspan class="headline__word"> enrolments now open!</tspan></text>

    <text class="subline" x="76" y="573" textLength="1056" lengthAdjust="spacingAndGlyphs">Get your child ready for school with us!</text>
  </svg>
</main>
</body>
</html>
```